Business Card + Stationery Design for a Craft Beer Bar

Mr. Tolvek's is a taproom sport bar that contains in its menu beers from different places around the world. What we offer differently is the experience that you can get inside our location, ambient music with rock from the 80s to 90s, projection with the sports of the moment, board games and private events.

Target Market(s)

Young people, Mid and High Class

Industry/Entity Type

Business

Font styles to use
Serif
Sans Serif

Colors
fee18a

Requirements
Must have
• Name, Title, Contact Details, Website
Nice to have
• Mail Signature
Should not have
• n/a

```html
<!DOCTYPE html>
<html lang="en">
<head>
<meta charset="utf-8">
<title>Mr. Tolvek's Taproom – Stationery</title>
<link rel="stylesheet" href="https://fonts.googleapis.com/css2?family=Oswald:wght@600&family=Raleway:wght@300;400&display=swap">
<style>
  :root {
    --backdrop: #dedede;
    --paper: #ffffff;
    --paper-shade: #f6f6f6;
    --brand-yellow: #edbd52;
    --ink: #1d1d1d;
    --ink-soft: #4a4a4a;
    --watermark: #d6d6d6;
    --rule: #9a9a9a;
  }
  * { box-sizing: border-box; margin: 0; padding: 0; }
  html, body { width: 1200px; height: 1000px; overflow: hidden; }
  body {
    position: relative;
    background: var(--backdrop);
    font-family: "Raleway", "Helvetica Neue", Arial, sans-serif;
    color: var(--ink);
  }
  .sheet {
    position: absolute;
    background: var(--paper);
    box-shadow: 0 10px 28px rgba(0,0,0,.14);
  }
  .wordmark {
    font-family: "Oswald", "Arial Narrow", sans-serif;
    font-weight: 600;
    letter-spacing: .5px;
    text-transform: uppercase;
    color: var(--ink);
    display: flex;
    align-items: center;
    gap: 8px;
    line-height: 1;
  }
  .wordmark .dot {
    width: 10px; height: 10px; border-radius: 50%;
    background: var(--brand-yellow);
    flex: none;
  }
  .contact-list { list-style: none; font-weight: 300; color: var(--ink-soft); }
  .contact-list li { display: flex; align-items: center; gap: 7px; }
  .contact-list svg { width: 11px; height: 11px; fill: var(--ink); flex: none; }

  /* Business card – front */
  .card-front {
    left: 60px; top: 110px; width: 340px; height: 200px;
    background: var(--brand-yellow);
    display: flex; align-items: center; justify-content: center;
  }
  .card-front .wordmark { font-size: 30px; }
  .card-front .wordmark .dot { background: var(--ink); }

  /* Business card – back */
  .card-back {
    left: 60px; top: 350px; width: 340px; height: 200px;
    display: flex; align-items: center;
  }
  .card-back .brand-side {
    width: 150px; display: flex; justify-content: center;
  }
  .card-back .wordmark { font-size: 18px; }
  .card-back .divider { width: 1px; height: 120px; background: var(--rule); }
  .card-back .details { padding-left: 18px; }
  .card-back .holder { font-weight: 400; font-size: 14px; margin-bottom: 10px; color: var(--ink-soft); }
  .card-back .contact-list li { font-size: 10.5px; margin-bottom: 6px; }

  /* Envelope */
  .envelope {
    left: 60px; top: 620px; width: 560px; height: 270px;
    padding: 28px 30px;
    display: flex; flex-direction: column; justify-content: space-between;
  }
  .envelope .wordmark { font-size: 22px; }
  .envelope .contact-list li { font-size: 10.5px; margin-bottom: 5px; }

  /* Letterhead */
  .letterhead {
    left: 660px; top: 110px; width: 480px; height: 780px;
    display: flex; flex-direction: column;
  }
  .letterhead .masthead { display: flex; justify-content: center; padding-top: 48px; }
  .letterhead .masthead .wordmark { font-size: 24px; }
  .letterhead .body-area {
    flex: 1; display: flex; align-items: center; justify-content: center;
  }
  .letterhead .watermark-name {
    font-family: "Oswald", "Arial Narrow", sans-serif;
    font-weight: 600; font-size: 56px; text-transform: uppercase;
    color: var(--watermark);
  }
  .letterhead .footer-band {
    height: 44px; background: var(--brand-yellow);
    padding: 0 22px;
  }
  .letterhead .footer-band .contact-list {
    height: 100%; display: flex; align-items: center; justify-content: space-between;
    color: var(--ink);
  }
  .letterhead .footer-band li { font-size: 10px; }
</style>
</head>
<body>

<svg width="0" height="0" style="position:absolute" aria-hidden="true">
  <symbol id="icon-pin" viewBox="0 0 12 12"><path d="M6 0a4 4 0 0 0-4 4c0 3 4 8 4 8s4-5 4-8a4 4 0 0 0-4-4zm0 5.6A1.6 1.6 0 1 1 6 2.4a1.6 1.6 0 0 1 0 3.2z"/></symbol>
  <symbol id="icon-phone" viewBox="0 0 12 12"><path d="M3 0h6a1 1 0 0 1 1 1v10a1 1 0 0 1-1 1H3a1 1 0 0 1-1-1V1a1 1 0 0 1 1-1zm0 1.5v8h6v-8z"/></symbol>
  <symbol id="icon-mail" viewBox="0 0 12 12"><path d="M0 2.5h12v7H0zm1 1v.3l5 3 5-3v-.3z"/></symbol>
  <symbol id="icon-web" viewBox="0 0 12 12"><path d="M6 0a6 6 0 1 0 0 12A6 6 0 0 0 6 0zm0 1c.7 0 1.5 1.6 1.7 4.5H4.3C4.5 2.6 5.3 1 6 1zM1 6.5h2.3c.1 1.8.4 3.3.9 4.2A5 5 0 0 1 1 6.5zm0-1a5 5 0 0 1 3.2-4.2c-.5.9-.8 2.4-.9 4.2zm5 5.5c-.7 0-1.5-1.6-1.7-4.5h3.4C7.5 9.4 6.7 11 6 11zm1.8-.3c.5-.9.8-2.4.9-4.2H11a5 5 0 0 1-3.2 4.2zm.9-5.2c-.1-1.8-.4-3.3-.9-4.2A5 5 0 0 1 11 5.5z"/></symbol>
</svg>

<section class="sheet card-front" aria-label="Business card front">
  <div class="wordmark"><span class="dot"></span>Mr. Tolvek's</div>
</section>

<section class="sheet card-back" aria-label="Business card back">
  <div class="brand-side"><div class="wordmark"><span class="dot"></span>Mr. Tolvek's</div></div>
  <div class="divider"></div>
  <div class="details">
    <p class="holder">Mr. Tolvek</p>
    <ul class="contact-list">
      <li><svg><use href="#icon-pin"/></svg>City, State Zip</li>
      <li><svg><use href="#icon-phone"/></svg>555 - 014 - 2290</li>
      <li><svg><use href="#icon-mail"/></svg>mtolvek@mrtolvek.com</li>
      <li><svg><use href="#icon-web"/></svg>www.mrtolvek.com</li>
    </ul>
  </div>
</section>

<section class="sheet envelope" aria-label="Envelope">
  <div class="wordmark"><span class="dot"></span>Mr. Tolvek's</div>
  <ul class="contact-list">
    <li><svg><use href="#icon-pin"/></svg>City, State Zip</li>
    <li><svg><use href="#icon-phone"/></svg>555 - 014 - 2290</li>
    <li><svg><use href="#icon-mail"/></svg>mtolvek@mrtolvek.com</li>
    <li><svg><use href="#icon-web"/></svg>www.mrtolvek.com</li>
  </ul>
</section>

<section class="sheet letterhead" aria-label="Letterhead">
  <header class="masthead"><div class="wordmark"><span class="dot"></span>Mr. Tolvek's</div></header>
  <div class="body-area"><span class="watermark-name">Mr. Tolvek's</span></div>
  <footer class="footer-band">
    <ul class="contact-list">
      <li><svg><use href="#icon-pin"/></svg>City, State Zip</li>
      <li><svg><use href="#icon-phone"/></svg>555 - 014 - 2290</li>
      <li><svg><use href="#icon-mail"/></svg>mtolvek@mrtolvek.com</li>
      <li><svg><use href="#icon-web"/></svg>www.mrtolvek.com</li>
    </ul>
  </footer>
</section>

</body>
</html>
```